Dodgeball League website

I require a nice, cool and attractive website for a new dodgeball league competition. I will need in PSD:

- Home Page
- Generic pages for news, about us etc
- Rank page with a table of team scores. stats etc

*Please design this with a Joomla*

I have attached:
- a logo
- site map for the links
- page layout guide

Example site for layout
http://www.velmorcircuit.com/

Design
Retro,cool feel, matches well with logo

Contact me if you have any questions

Reason: Would like to see a few more designs

Target Market(s)

Young adults 18 - 35.

Industry/Entity Type

News

Colors

Designer to choose colors to be used in the design.

Requirements
Must have
• I want a cool, retro feel to the website. Not to picky on the colors. Something that will match nicely with the logo given. I will give feedback on it.
Calm colors not too bright and overwhelming
Nice to have
• Include some pictures within the picture slider so I can get a feel for the website.
Nice clean background
Should not have
• To much clutter of text
Do not put pictures in the background.

```html
<!DOCTYPE html>
<html lang="en">
<head>
<meta charset="utf-8">
<title>Rallyline Dodgeball League</title>
<link href="https://fonts.googleapis.com/css2?family=Oswald:wght@400;600&family=Open+Sans:wght@400;600;700&display=swap" rel="stylesheet">
<style>
:root{
  --bg:#e8d3a4;
  --paper:#f5e8c8;
  --paper-dark:#ead8ad;
  --red:#b5321d;
  --red-dark:#8e2413;
  --orange:#e2772a;
  --ink:#2c2520;
  --muted:#7a6a55;
  --line:#d6c193;
  --blue:#3b5a98;
}
*{box-sizing:border-box;margin:0;padding:0}
html,body{width:793px;height:1200px;overflow:hidden}
body{background:var(--bg);font-family:"Open Sans",Arial,sans-serif;color:var(--ink);font-size:8px;position:relative}
.page{position:absolute;left:20px;top:0;width:753px;height:1200px;background:linear-gradient(180deg,var(--paper),#f1e1bb 60%,var(--paper));box-shadow:0 0 12px rgba(90,60,20,.25)}
.abs{position:absolute}
h2,h3{font-family:"Oswald",Arial,sans-serif;font-weight:600}

/* header */
.brand{left:14px;top:20px;width:180px;height:130px;display:flex;align-items:center;gap:8px}
.brand-dot{width:44px;height:44px;border-radius:50%;background:var(--orange);flex:none}
.brand-name{font-family:"Oswald",Arial,sans-serif;font-weight:600;color:var(--red);font-size:20px;line-height:1.05;text-transform:uppercase}
.mini-table{top:14px;width:134px;border-collapse:collapse;font-size:6.5px;color:var(--muted)}
.mini-table th{color:var(--red);font-weight:700;text-align:left;padding:3px 4px;border-bottom:1px solid var(--line)}
.mini-table td{padding:4px;border-bottom:1px dotted var(--line)}
.mini-table td+td,.mini-table th+th{text-align:center}

/* nav */
.nav{left:10px;top:164px;width:733px;height:22px;background:linear-gradient(var(--red),var(--red-dark));display:flex;align-items:center;padding:0 6px;gap:2px}
.nav a{color:#fff;text-decoration:none;font-size:7.5px;font-weight:600;padding:4px 8px}
.nav a.active{background:var(--orange);border-radius:2px}
.search{margin-left:auto;width:110px;height:14px;background:#fff;border-radius:2px;font-size:6.5px;color:#999;padding:2px 5px;display:flex;justify-content:space-between}

/* slider */
.slider{left:10px;top:190px;width:733px;height:246px;background:linear-gradient(120deg,#6a3f22,#c07a3a 55%,#8a5a33);overflow:hidden}
.caption{left:22px;top:126px;width:300px;color:#fff}
.caption h2{font-size:13px;font-weight:600;line-height:1.2;text-shadow:0 1px 2px rgba(0,0,0,.5)}
.caption p{font-size:7px;margin:3px 0 6px;opacity:.9}
.btn{display:inline-block;background:var(--red);color:#fff;font-size:7px;font-weight:700;padding:3px 8px;border-radius:2px}
.dots{right:16px;bottom:12px;display:flex;gap:4px}
.dots span{width:6px;height:6px;border-radius:50%;background:rgba(255,255,255,.5)}
.dots span:first-child{background:#fff}

/* news */
.section-title{font-size:11px;color:var(--red)}
.news{left:14px;top:448px;width:490px}
.news-item{display:flex;gap:10px;margin-top:9px;padding-bottom:7px;border-bottom:1px dotted var(--line)}
.thumb{width:62px;height:42px;background:linear-gradient(135deg,#7a4a2a,#c98a4b);flex:none}
.news-item h3{font-size:8px;color:var(--red);font-family:"Open Sans",Arial,sans-serif;font-weight:700}
.news-item .date{color:var(--muted);font-size:6.5px}
.news-item p{font-size:6.5px;color:var(--muted);line-height:1.35}
.more{font-size:6.5px;color:var(--ink);font-weight:700}
.view-all{text-align:right;font-size:6.5px;color:var(--muted);margin-top:4px}

/* right column */
.like-box{left:532px;top:452px;width:200px;text-align:center}
.like-box .tag{display:inline-block;background:var(--ink);color:#fff;font-size:6.5px;font-weight:700;padding:2px 8px}
.like-box .net{font-size:18px;font-weight:700;color:var(--blue)}
.register{left:532px;top:505px;width:200px;height:140px;border:1px dashed var(--muted);text-align:center;padding:8px}
.register .kicker{color:var(--red);font-weight:700;font-size:8px}
.register .title{font-size:9px;font-weight:700}
.register .mark{width:46px;height:46px;border-radius:50%;background:var(--orange);margin:8px auto}
.register .btn{font-size:8px;padding:4px 14px}

.social{left:532px;top:656px;width:200px;height:126px;background:#fff;border:1px solid var(--line);padding:7px}
.social-head{display:flex;gap:6px;align-items:center}
.social-head .sq{width:22px;height:22px;background:var(--orange)}
.social-head b{font-size:8px;color:var(--blue)}
.like-btn{display:inline-block;border:1px solid #ccc;font-size:6px;padding:1px 4px;margin-top:2px;color:var(--ink)}
.social p{font-size:6px;color:var(--muted);margin:6px 0 4px}
.faces{display:grid;grid-template-columns:repeat(5,1fr);gap:4px}
.faces span{height:26px;background:linear-gradient(#cfcfcf,#a9a9a9)}
.map{left:532px;top:788px;width:200px;height:62px;background:linear-gradient(135deg,#e6e3d9,#cfd8c4 60%,#d9d4c4);border:1px solid var(--line)}

/* league */
.league{left:14px;top:646px;width:500px}
.league-tabs{display:flex;height:22px;background:var(--ink);color:#fff;font-family:"Oswald",Arial,sans-serif;font-size:9px}
.league-tabs div{flex:1;display:flex;align-items:center;justify-content:center}
.league-tabs div:first-child{background:var(--red)}
.league table{width:100%;border-collapse:collapse;font-size:7.5px}
.league th{background:var(--paper-dark);text-align:left;padding:5px 10px;font-weight:700;color:var(--red)}
.league td{padding:6px 10px;border-bottom:1px solid var(--line);color:var(--muted)}
.league tr:nth-child(even) td{background:rgba(255,255,255,.35)}
.league .r{text-align:right}

/* top 3 */
.top3{top:868px;width:232px}
.top3 h3{font-size:10px;color:var(--red);margin-bottom:4px}
.top3 table{width:100%;border-collapse:collapse;font-size:6.5px}
.top3 th{background:var(--paper-dark);text-align:left;padding:4px;font-weight:700}
.top3 td{padding:5px 4px;border-bottom:1px dotted var(--line);color:var(--muted)}

/* sponsors */
.sponsors{left:14px;top:1068px;width:725px;height:66px;display:flex;gap:14px;align-items:center;border-top:1px solid var(--line);border-bottom:1px solid var(--line)}
.sponsor{flex:1;height:48px;display:flex;align-items:center;justify-content:center;gap:6px;font-weight:700;font-size:11px;color:var(--ink)}
.sponsor .sq{width:16px;height:16px;background:var(--ink)}
.sponsor .badge{width:80px;height:40px;border-radius:50%;background:#3c6e8f}
.footer{left:14px;top:1150px;width:725px;display:flex;justify-content:space-between;font-size:6.5px;color:var(--muted)}
</style>
</head>
<body>
<div class="page">

  <header>
    <div class="abs brand">
      <span class="brand-dot"></span>
      <span class="brand-name">Rallyline<br>Dodgeball<br>League</span>
    </div>
    <table class="abs mini-table" style="left:218px">
      <tr><th>Last Season</th><th>Pts</th><th>Sets</th></tr>
      <tr><td>Team 1</td><td>3</td><td>5</td></tr>
      <tr><td>Team 2</td><td>3</td><td>4</td></tr>
      <tr><td>Team 3</td><td>2</td><td>3</td></tr>
      <tr><td>Team 4</td><td>1</td><td>2</td></tr>
    </table>
    <table class="abs mini-table" style="left:376px">
      <tr><th>Last Season</th><th>Pts</th><th>Sets</th></tr>
      <tr><td>Team 1</td><td>3</td><td>5</td></tr>
      <tr><td>Team 2</td><td>3</td><td>4</td></tr>
      <tr><td>Team 3</td><td>2</td><td>3</td></tr>
      <tr><td>Team 4</td><td>1</td><td>2</td></tr>
    </table>
    <table class="abs mini-table" style="left:534px">
      <tr><th>Last Season</th><th>Pts</th><th>Sets</th></tr>
      <tr><td>Team 1</td><td>3</td><td>5</td></tr>
      <tr><td>Team 2</td><td>3</td><td>4</td></tr>
      <tr><td>Team 3</td><td>2</td><td>3</td></tr>
      <tr><td>Team 4</td><td>1</td><td>2</td></tr>
    </table>
  </header>

  <nav class="abs nav">
    <a class="active">Home</a><a>About Us</a><a>Team</a><a>Schedule</a><a>News</a><a>Photos &amp; Videos</a><a>Register</a><a>Contact Us</a>
    <div class="search"><span>Search...</span><span>&#9906;</span></div>
  </nav>

  <section class="abs slider" role="img" aria-label="Slider photo: player in a red shirt holding a dodgeball in a gym">
    <div class="abs caption">
      <h2>Neque porro quisquem est qui dolorem ipsum quia dolor sit amet</h2>
      <p>Consectetur adipisci velit sed quia non numquam eius modi tempora.</p>
      <span class="btn">Read More</span>
    </div>
    <div class="abs dots"><span></span><span></span><span></span></div>
  </section>

  <section class="abs news">
    <h2 class="section-title">Latest News</h2>
    <article class="news-item">
      <div class="thumb" role="img" aria-label="News photo of a match"></div>
      <div><h3>Match Wilson On Brink Of Qualifying</h3><div class="date">22.10.2013</div><p>Lorem ipsum dolor sit amet, consectetur adipiscing elit sed do.</p><span class="more">Read More »</span></div>
    </article>
    <article class="news-item">
      <div class="thumb" role="img" aria-label="News photo of a match"></div>
      <div><h3>Match Wilson On Brink Of Qualifying</h3><div class="date">22.10.2013</div><p>Lorem ipsum dolor sit amet, consectetur adipiscing elit sed do.</p><span class="more">Read More »</span></div>
    </article>
    <article class="news-item">
      <div class="thumb" role="img" aria-label="News photo of a match"></div>
      <div><h3>Match Wilson On Brink Of Qualifying</h3><div class="date">22.10.2013</div><p>Lorem ipsum dolor sit amet, consectetur adipiscing elit sed do.</p><span class="more">Read More »</span></div>
    </article>
  </section>

  <aside>
    <div class="abs like-box"><span class="tag">LIKE US ON</span><div class="net">Friendwall</div></div>
    <div class="abs register">
      <div class="kicker">• Register Dodgeball •</div>
      <div class="title">Rallyline dodgeball league</div>
      <div class="mark"></div>
      <span class="btn">Register Here</span>
    </div>
    <div class="abs social">
      <div class="social-head"><span class="sq"></span><div><b>Rallyline dodgeball league</b><br><span class="like-btn">Like</span></div></div>
      <p>1,071 people like Rallyline dodgeball league.</p>
      <div class="faces" role="img" aria-label="Grid of fan profile pictures"><span></span><span></span><span></span><span></span><span></span><span></span><span></span><span></span><span></span><span></span></div>
    </div>
    <div class="abs map" role="img" aria-label="Map showing the league venue location"></div>
  </aside>

  <section class="abs league">
    <div class="league-tabs"><div>Rallyline Rubber League</div><div>Rallyline Foam League</div></div>
    <table>
      <tr><th>Rank</th><th>Team Name</th><th class="r">Score</th></tr>
      <tr><td>01</td><td>Lorem ipsum dolor sit amet</td><td class="r">125</td></tr>
      <tr><td>02</td><td>Consectetur adipiscing elit</td><td class="r">118</td></tr>
      <tr><td>03</td><td>Sed do eiusmod tempor incididunt</td><td class="r">104</td></tr>
      <tr><td>04</td><td>Ut labore et dolore magna</td><td class="r">97</td></tr>
      <tr><td>05</td><td>Ut enim ad minim veniam</td><td class="r">88</td></tr>
      <tr><td>06</td><td>Quis nostrud exercitation</td><td class="r">76</td></tr>
    </table>
    <div class="view-all">View All »</div>
  </section>

  <section class="abs top3" style="left:14px">
    <h3>TOP 3 KILLER</h3>
    <table>
      <tr><th>Rank</th><th>Name</th><th>Team</th><th>Score</th></tr>
      <tr><td>01</td><td>Lorem Ipsum</td><td>Lorem Team</td><td>32</td></tr>
      <tr><td>02</td><td>Dolor Amet</td><td>Lorem Team</td><td>28</td></tr>
      <tr><td>03</td><td>Sed Tempor</td><td>Lorem Team</td><td>25</td></tr>
    </table>
  </section>
  <section class="abs top3" style="left:260px">
    <h3>TOP 3 CATCHER</h3>
    <table>
      <tr><th>Rank</th><th>Name</th><th>Team</th><th>Score</th></tr>
      <tr><td>01</td><td>Lorem Ipsum</td><td>Lorem Team</td><td>30</td></tr>
      <tr><td>02</td><td>Dolor Amet</td><td>Lorem Team</td><td>27</td></tr>
      <tr><td>03</td><td>Sed Tempor</td><td>Lorem Team</td><td>21</td></tr>
    </table>
  </section>
  <section class="abs top3" style="left:507px">
    <h3>TOP 3 DODGER</h3>
    <table>
      <tr><th>Rank</th><th>Name</th><th>Team</th><th>Score</th></tr>
      <tr><td>01</td><td>Lorem Ipsum</td><td>Lorem Team</td><td>34</td></tr>
      <tr><td>02</td><td>Dolor Amet</td><td>Lorem Team</td><td>29</td></tr>
      <tr><td>03</td><td>Sed Tempor</td><td>Lorem Team</td><td>24</td></tr>
    </table>
  </section>

  <section class="abs sponsors">
    <div class="sponsor">Harbor Lane Pub &amp; Grill</div>
    <div class="sponsor"><span class="sq"></span>Norvale</div>
    <div class="sponsor"><span class="badge"></span></div>
    <div class="sponsor">Kestra TV</div>
    <div class="sponsor"><span class="sq"></span>Brightmark</div>
  </section>

  <footer class="abs footer">
    <span>Copyright © 2013 Rallyline Dodgeball League.com. All Rights Reserved</span>
    <span>Privacy Policy | Terms of Use</span>
  </footer>

</div>
</body>
</html>
```